Need a flyer to leave behind when visiting clients or at shows

Glossy colorful tri-fold flyer with the same information that is on my web site www.brevalinkpro.com. I am open to a little modern or creative take on the typical brochure. I created the web site so I can provide any raw files needed from it. I would also like the ability to edit this flyer in the future in Adobe Photoshop Elements

```html
<!DOCTYPE html>
<html lang="en">
<head>
<meta charset="utf-8">
<title>BrevaLink Pro Solutions – Tri-fold Brochure</title>
<link href="https://fonts.googleapis.com/css2?family=Open+Sans:ital,wght@0,400;0,600;0,700;1,700;1,800&family=Lato:wght@400;700&display=swap" rel="stylesheet">
<style>
  :root{
    --purple:#6b3fa3;
    --purple-light:#8a5cc4;
    --ink:#2b2b33;
    --muted:#55555f;
    --paper:#ffffff;
    --backdrop:#e4e4e6;
  }
  *{box-sizing:border-box;margin:0;padding:0}
  html,body{width:933px;height:1200px;overflow:hidden;background:var(--backdrop)}
  body{position:relative;font-family:'Lato',sans-serif;color:var(--ink)}
  .spread{position:absolute;left:26px;width:880px;height:560px;background:var(--paper);box-shadow:0 6px 18px rgba(0,0,0,.18);overflow:hidden}
  .spread--outside{top:20px}
  .spread--inside{top:620px}
  .spread__art{position:absolute;inset:0;width:880px;height:560px}
  .fold{stroke:rgba(0,0,0,.06);stroke-width:1}
  .t{position:absolute}
  .heading{font-family:'Open Sans',sans-serif;font-weight:800;font-style:italic;color:var(--purple)}
  .sub{font-family:'Open Sans',sans-serif;font-weight:700;font-style:italic;color:var(--ink);font-size:15px}
  .body{font-size:11px;line-height:1.4;color:var(--muted)}
  /* outside */
  .about__tab{left:22px;top:248px;font-family:'Open Sans',sans-serif;font-weight:800;font-style:italic;color:#fff;font-size:20px}
  .about__list{left:26px;top:298px;width:245px}
  .about__list .sub{margin-top:12px}
  .about__list .sub:first-child{margin-top:0}
  .brand{left:610px;top:26px;display:flex;align-items:center;gap:8px;color:#fff;font-family:'Open Sans',sans-serif;font-weight:700;font-size:22px}
  .brand__mark{width:14px;height:14px;background:#fff}
  .cover__headline{left:610px;top:118px;width:255px;font-size:20px;line-height:1.2}
  .cover__tagline{left:610px;top:196px;width:250px;font-size:11px;color:var(--ink)}
  .contact{left:318px;top:330px;color:#fff}
  .contact__title{font-family:'Open Sans',sans-serif;font-weight:700;font-size:24px}
  .contact__phone{font-family:'Open Sans',sans-serif;font-weight:700;font-size:22px;display:flex;align-items:center;gap:6px;margin-top:6px}
  .contact__email{font-size:12px;display:flex;align-items:center;gap:8px;margin-top:14px}
  /* inside */
  .values{left:26px;top:205px}
  .values__title{font-family:'Open Sans',sans-serif;font-weight:700;color:var(--purple);font-size:17px;letter-spacing:.3px}
  .values ul,.it-list ul{list-style:none;margin-top:8px}
  .values li,.it-list li{font-size:9.5px;color:var(--ink);margin-bottom:5px;display:flex;align-items:center;gap:7px;text-transform:uppercase}
  .it-list li{text-transform:none;font-size:10px}
  .dot{width:7px;height:7px;border:1.3px solid var(--muted);border-radius:50%;flex:none}
  .services-left{left:26px;top:360px;width:255px}
  .row{display:flex;align-items:center;gap:12px;margin-top:12px;font-size:10.5px;color:var(--ink)}
  .row__icon{width:30px;height:26px;border-radius:7px;background:var(--purple);flex:none;display:flex;align-items:center;justify-content:center}
  .bio__name{left:412px;top:26px;font-family:'Open Sans',sans-serif;font-weight:700;font-style:italic;font-size:10.5px}
  .bio__role{left:412px;top:40px;font-size:9px;font-weight:700}
  .bio__text{left:306px;top:150px;width:268px;font-size:10px;line-height:1.45;color:var(--ink);text-align:justify}
  .services-right{left:604px;top:190px;width:262px}
  .services-right .heading{font-size:20px}
  .services-right .body{margin-top:6px;color:var(--ink);font-size:10px}
  .it-list{left:604px;top:298px}
  .it-list .heading{font-size:14px}
  .url{left:700px;top:520px;color:#fff;font-size:10px;letter-spacing:1.5px}
</style>
</head>
<body>

<section class="spread spread--outside">
  <svg class="spread__art" viewBox="0 0 880 560">
    <defs>
      <linearGradient id="g-team" x1="0" y1="0" x2="1" y2="1"><stop offset="0" stop-color="#b9a48c"/><stop offset="1" stop-color="#5d5a5f"/></linearGradient>
      <linearGradient id="g-med" x1="0" y1="0" x2="1" y2="0"><stop offset="0" stop-color="#e9eef3"/><stop offset="1" stop-color="#a9c3d8"/></linearGradient>
      <linearGradient id="g-meet" x1="0" y1="0" x2="1" y2="1"><stop offset="0" stop-color="#c9d6b8"/><stop offset="1" stop-color="#4d4b55"/></linearGradient>
    </defs>
    <path role="img" aria-label="Photo of a team reviewing charts at a desk" fill="url(#g-team)" d="M0 0H293V150Q200 160 150 185Q80 220 0 215Z"/>
    <path fill="var(--purple)" d="M0 215Q80 220 150 185Q200 160 293 150V172Q210 182 160 208Q90 242 0 240Z"/>
    <path fill="var(--purple)" d="M14 246H150L140 280H14Z"/>
    <path fill="var(--purple)" d="M0 525Q160 530 293 470V505Q180 545 0 545Z"/>
    <circle cx="440" cy="60" r="26" fill="#c9c9d3"/>
    <path fill="var(--purple)" d="M293 125Q440 150 587 105V120Q440 165 293 145Z"/>
    <path role="img" aria-label="Illustration of a clinician with medical icons" fill="url(#g-med)" d="M293 145Q440 165 587 120V270H293Z"/>
    <path fill="var(--purple)" d="M293 300Q340 272 420 270H587V470Q450 468 293 510Z"/>
    <path fill="var(--purple)" d="M587 0H880V88Q770 62 670 92Q625 104 587 90Z"/>
    <path fill="var(--purple-light)" d="M587 100Q640 112 700 100Q800 82 880 96V104Q800 92 700 108Q640 120 587 108Z"/>
    <path role="img" aria-label="Photo of business people in a friendly meeting" fill="url(#g-meet)" d="M587 240H880V440H587Z"/>
    <path fill="var(--purple)" d="M587 300Q600 360 660 440H587Z"/>
    <line class="fold" x1="293" y1="0" x2="293" y2="560"/>
    <line class="fold" x1="587" y1="0" x2="587" y2="560"/>
  </svg>

  <div class="t about__tab">About Us</div>
  <div class="t about__list">
    <div class="sub">Our Mission</div>
    <p class="body">Partner with clients to increase the value and security of their technology tools.</p>
    <div class="sub">Our Goal</div>
    <p class="body">Become the premiere consulting company for Information Technology in the post-acute care industries.</p>
    <div class="sub">Our Leaders</div>
    <p class="body"><strong>Darren Holt</strong>, MHA, MBA</p>
  </div>

  <div class="t contact">
    <div class="contact__title">Contact Us</div>
    <div class="contact__phone">
      <svg width="16" height="16" viewBox="0 0 16 16"><circle cx="8" cy="8" r="8" fill="#fff"/><path d="M5 4.5l1.5-.5 1 2-1 .8a5 5 0 0 0 2.7 2.7l.8-1 2 1-.5 1.5C9 11.5 4.5 7 5 4.5Z" fill="var(--purple)"/></svg>
      555-014-2290
    </div>
    <div class="contact__email">
      <svg width="11" height="11" viewBox="0 0 12 12"><circle cx="6" cy="6" r="6" fill="#fff"/><rect x="3" y="4" width="6" height="4" fill="var(--purple)"/></svg>
      dholt@brevalinkpro.com
    </div>
  </div>

  <div class="t brand"><span class="brand__mark"></span>BrevaLink Pro</div>
  <h1 class="t heading cover__headline">Increasing The Value and Security of Your Technology Resources</h1>
  <p class="t cover__tagline">Providing Information Technology expertise to post-acute care providers</p>
</section>

<section class="spread spread--inside">
  <svg class="spread__art" viewBox="0 0 880 560">
    <defs>
      <linearGradient id="g-desk" x1="0" y1="0" x2="1" y2="1"><stop offset="0" stop-color="#f1e4e6"/><stop offset="1" stop-color="#c7c3cf"/></linearGradient>
      <linearGradient id="g-it" x1="0" y1="0" x2="1" y2="0"><stop offset="0" stop-color="#3b4f7a"/><stop offset="1" stop-color="#8aa6cf"/></linearGradient>
      <linearGradient id="g-lab" x1="0" y1="0" x2="1" y2="0"><stop offset="0" stop-color="#dfe7ef"/><stop offset="1" stop-color="#b8c3cf"/></linearGradient>
    </defs>
    <path role="img" aria-label="Photo of a person using a phone beside a laptop" fill="url(#g-desk)" d="M0 0H293V175H0Z"/>
    <path fill="var(--purple)" d="M0 176H293V188Q150 198 0 200Z"/>
    <path fill="var(--purple)" d="M0 322Q150 330 293 318V336Q150 348 0 342Z"/>
    <rect x="320" y="22" width="82" height="92" rx="14" fill="#b4b4bd" role="img" aria-label="Portrait of the president and CEO"/>
    <circle cx="440" cy="92" r="20" fill="#c9c9d3"/>
    <path role="img" aria-label="Photo of IT professional touching a digital interface" fill="url(#g-it)" d="M587 0H880V120Q800 140 700 150Q640 155 587 130Z"/>
    <path fill="var(--purple)" d="M587 130Q640 155 700 150Q800 140 880 120V134Q800 156 700 164Q640 166 587 142Z"/>
    <path fill="var(--purple)" d="M293 395Q450 350 587 380V394Q450 366 293 410Z"/>
    <path role="img" aria-label="Photo of smiling medical staff in a clinic" fill="url(#g-lab)" d="M293 410Q450 366 587 394V560H293Z"/>
    <path fill="var(--purple)" d="M660 560Q668 505 740 492H880V560Z"/>
    <line class="fold" x1="293" y1="0" x2="293" y2="560"/>
    <line class="fold" x1="587" y1="0" x2="587" y2="560"/>
  </svg>

  <div class="t values">
    <div class="values__title">OUR CORE VALUES</div>
    <ul>
      <li><span class="dot"></span>Client Focused</li>
      <li><span class="dot"></span>Accountability</li>
      <li><span class="dot"></span>Integrity</li>
      <li><span class="dot"></span>Professional Development</li>
    </ul>
  </div>

  <div class="t services-left">
    <div class="heading" style="font-size:20px">Our Services</div>
    <div class="row"><span class="row__icon"><svg width="14" height="14" viewBox="0 0 14 14"><circle cx="7" cy="5" r="3" fill="#fff"/><rect x="2" y="9" width="10" height="4" rx="2" fill="#fff"/></svg></span>Understand and exceed client expectations</div>
    <div class="row"><span class="row__icon"><svg width="16" height="12" viewBox="0 0 16 12"><path d="M1 6h14M5 3l-4 3 4 3M11 3l4 3-4 3" stroke="#fff" stroke-width="1.6" fill="none"/></svg></span>Committed to be a partner, not vendor</div>
    <div class="row"><span class="row__icon"><svg width="14" height="14" viewBox="0 0 14 14"><circle cx="7" cy="7" r="5" stroke="#fff" stroke-width="1.6" fill="none"/><path d="M7 4v3l2 2" stroke="#fff" stroke-width="1.6" fill="none"/></svg></span>Provide simplified change management expertise</div>
  </div>

  <div class="t bio__name">Darren Holt, MHA, MBA, CHCIO</div>
  <div class="t bio__role">President and CEO</div>
  <p class="t bio__text">Darren is the founder and CEO of BrevaLink Pro Solutions. He has been working in the technology industry for over 25 years with extensive experience in healthcare IT. Darren has held multiple roles including Chief Information Officer, Chief Information Security Officer, and the executive sponsor of multiple electronic health record (EHR) implementations. He has created and nurtured numerous successful IT departments and built strong relationships with leadership teams. Darren holds a Master's in Business Administration and a Master's in Healthcare Administration, and is certified with the Healthcare IT Leadership Council (HITLC).</p>

  <div class="t services-right">
    <div class="heading">Our Services</div>
    <p class="body">We understand different organizations have different needs. BrevaLink Pro strives to assist your organization by bringing solutions that are easy to understand and allow the client to track success. We provide solutions based on the client's needs and desires.</p>
  </div>

  <div class="t it-list">
    <div class="heading">Information Technology</div>
    <ul>
      <li><span class="dot"></span>CIO or IT Director Services</li>
      <li><span class="dot"></span>CISO or Information Security Officer</li>
      <li><span class="dot"></span>Comprehensive ePHI Risk Assessments</li>
      <li><span class="dot"></span>IT Department Evaluation</li>
      <li><span class="dot"></span>Policy Management and Consulting</li>
      <li><span class="dot"></span>On-going IT department support</li>
    </ul>
  </div>

  <div class="t url">www.brevalinkpro.com</div>
</section>

</body>
</html>
```